Brasko Construction Business Card

I need a business card design for my company.
We are a construction/machinery company.
I would like to see my logo on the front of the card and my details on the other side
I would like the card to be black or dark grey in colour,with my logo as i send it or modified with a lighter blue colour
I would like to see the design kept fairly simple,but eye catching at the same time
Industry/Entity Type
Business
Contact Information for Business Card
Name
Phone Number
Address
Email
Colors
00a990
1b1b1b
000000
474747
ececec

```html
<!DOCTYPE html>
<html lang="en">
<head>
<meta charset="utf-8">
<title>Brasko Construction Business Card</title>
<link href="https://fonts.googleapis.com/css2?family=Exo+2:wght@400;700&display=swap" rel="stylesheet">
<style>
  :root {
    --teal: #00a990;
    --ink: #000000;
    --charcoal: #1b1b1b;
    --graphite: #474747;
    --paper: #ececec;
    --silver: #bdbab5;
    --stage: #e4e2df;
  }
  * { box-sizing: border-box; margin: 0; padding: 0; }
  html, body {
    width: 1200px; height: 1000px; overflow: hidden;
    background: var(--stage);
    font-family: "Exo 2", sans-serif;
  }
  .sheet {
    width: 1200px; height: 1000px;
    display: flex; flex-direction: column; align-items: center; justify-content: center; gap: 64px;
  }
  .card {
    position: relative;
    width: 700px; height: 400px;
    background: linear-gradient(135deg, var(--charcoal) 0%, var(--ink) 55%);
    box-shadow: 0 10px 30px rgba(0,0,0,.25);
    overflow: hidden;
    color: var(--paper);
  }
  /* front */
  .brand {
    position: absolute; left: 0; right: 0; top: 120px;
    display: flex; align-items: center; justify-content: center; gap: 22px;
  }
  .brand-mark { width: 64px; height: 64px; background: var(--paper); }
  .brand-name {
    font-weight: 700; color: var(--paper); text-transform: uppercase; line-height: 1;
  }
  .brand-name .line-one { display: block; font-size: 78px; letter-spacing: 4px; }
  .brand-name .line-two { display: block; font-size: 30px; letter-spacing: 7px; margin-top: 8px; }
  .website {
    position: absolute; right: 44px; bottom: 36px;
    font-size: 20px; letter-spacing: .5px; color: var(--paper);
  }
  /* back */
  .back-logo {
    position: absolute; left: 0; top: 0; width: 230px; height: 96px;
    display: flex; align-items: center; gap: 10px; padding-left: 28px;
    background: var(--charcoal);
    border-top: 8px solid var(--teal);
  }
  .back-logo .brand-mark { width: 26px; height: 26px; }
  .back-logo .brand-name .line-one { font-size: 28px; letter-spacing: 2px; }
  .back-logo .brand-name .line-two { font-size: 11px; letter-spacing: 2.6px; margin-top: 3px; }
  .band-silver {
    position: absolute; left: 230px; right: 0; top: 18px; height: 44px;
    background: linear-gradient(90deg, var(--silver), var(--paper) 60%, var(--silver));
  }
  .band-teal {
    position: absolute; left: 230px; right: 0; top: 62px; height: 20px;
    background: var(--teal);
  }
  .person {
    position: absolute; left: 200px; top: 150px;
    font-weight: 700; font-size: 40px; letter-spacing: 3px; text-transform: uppercase;
  }
  .address {
    position: absolute; left: 250px; top: 222px;
    font-size: 21px; line-height: 1.2; color: var(--paper);
  }
  .contact {
    position: absolute; left: 40px; bottom: 36px;
    list-style: none; font-size: 20px; line-height: 1.6;
  }
  .contact li { display: flex; align-items: center; gap: 12px; }
  .contact svg { width: 18px; height: 18px; flex: none; }
</style>
</head>
<body>
<main class="sheet">
  <section class="card card-front" aria-label="Card front">
    <div class="brand">
      <span class="brand-mark"></span>
      <span class="brand-name"><span class="line-one">Brasko</span><span class="line-two">Construction</span></span>
    </div>
    <p class="website">www.yoursitehere.com.au</p>
  </section>

  <section class="card card-back" aria-label="Card back">
    <div class="back-logo">
      <span class="brand-mark"></span>
      <span class="brand-name"><span class="line-one">Brasko</span><span class="line-two">Construction</span></span>
    </div>
    <div class="band-silver"></div>
    <div class="band-teal"></div>
    <h1 class="person">Your Name</h1>
    <p class="address">1234 your adress<br>here your adress<br>here your adres</p>
    <ul class="contact">
      <li>
        <svg viewBox="0 0 18 18" aria-hidden="true"><rect x="4" y="1" width="10" height="16" rx="2" fill="none" stroke="#ececec" stroke-width="1.6"/><line x1="8" y1="14" x2="10" y2="14" stroke="#ececec" stroke-width="1.6"/></svg>
        012 345 6789
      </li>
      <li>
        <svg viewBox="0 0 18 18" aria-hidden="true"><rect x="1" y="4" width="16" height="11" fill="none" stroke="#ececec" stroke-width="1.6"/><polyline points="1,4 9,10 17,4" fill="none" stroke="#ececec" stroke-width="1.6"/></svg>
        your.name@brasko.com
      </li>
    </ul>
  </section>
</main>
</body>
</html>
```